Texas Marsh Reed Conservation League

We need to design the home page of this new website. We would like a fun website design for provides as a resource for members and information for potential members.
Please design so that we can see a portion of background on each side on the website.
I just need the final design files psd no coding needed.
Attached is their logo (colors are not 100% set in stone either so can mess with those as I did in the quick mockup attached)
Attached is a pdf newsletter they send out, you can get a feel for them and what they are about. The design is crappy and we are here to fix that going forward and we are starting with the website.
Here are some quick example websites (design style is open)
- I attached a quick mockup i did just for a content visual but by all means do what you want.
- http://www.lonestarbizladies.org/
- http://www.wqrtf.org/
- http://demo.webkitpalette.com/demo.php?cat=html5themes&host=layoutbazaar&temp=veltrona
- http://www.fieldkeep.org/
- http://www.urbanpantry.org/
- http://www.projectcozy.org/
here are some of the other chapters website (pretty bad!)
and here are some of the others:
- http://www.kdwrcl.org/
- http://wrcl.org/
- http://www.gwrcl.org/
Content Items that need to be included:
1. Logo
2. Menu - home, about, members, resources, events, membership, contact
3. Become a member - button or action
4. social links - facebook, linkedin, youtube
5. banner - that needs to explain their purpose "Promoting environmental stewardship through operations, research, education and outreach" (or this can be worked into the design)
6. Upcoming event (s)
7. Advertisement - members can place an ad on the website, this can be a placeholder for now
8. newsletter signup
9. advertise with us - this link can be in the footer
30-60 years of age, succesfull (household budgets of 120K+ men and women that live in texas.
Education

```html
<!DOCTYPE html>
<html lang="en">
<head>
<meta charset="utf-8">
<title>Texas Marsh Reed Conservation League</title>
<link href="https://fonts.googleapis.com/css2?family=Lato:wght@300;400;700&family=Alfa+Slab+One&family=Montserrat:wght@700&display=swap" rel="stylesheet">
<style>
  :root{
    --sky-top:#5b86b0;
    --sky-glow:#f4f0c8;
    --field-green:#5f8a22;
    --field-dark:#2e4a12;
    --soil:#8a5a35;
    --panel:#333331;
    --header-panel:#3b3a33;
    --rule:#4a4a48;
    --text-muted:#8d8d8a;
    --text-light:#e6e6e2;
    --white:#ffffff;
    --accent-yellow:#f3c23a;
    --accent-yellow-light:#ffe07a;
    --nav-active:#f5d531;
    --button-grey-top:#ffffff;
    --button-grey-bottom:#cfcfcf;
  }
  *{box-sizing:border-box;margin:0;padding:0}
  html,body{width:1194px;height:1200px;overflow:hidden}
  body{
    position:relative;
    font-family:'Lato',sans-serif;
    background:
      radial-gradient(ellipse 420px 320px at 40px 240px, rgba(255,250,190,.95), rgba(255,250,190,0) 70%),
      linear-gradient(180deg,var(--sky-top) 0%,#9dbad0 14%,var(--sky-glow) 30%,#c9d65a 38%,var(--field-green) 50%,var(--field-dark) 72%,var(--soil) 84%,#3d3a2a 100%);
  }
  .site{
    position:absolute;left:179px;top:54px;width:836px;height:1146px;
    background:var(--panel);
  }
  .site-header{
    position:absolute;left:0;top:0;width:836px;height:472px;
    background:var(--header-panel);
  }
  .logo{
    position:absolute;left:29px;top:30px;display:flex;align-items:center;gap:8px;
    font-weight:700;font-size:44px;color:var(--white);letter-spacing:1px;
  }
  .logo-dot{width:22px;height:22px;border-radius:50%;background:#c8364a}
  .org-name{
    position:absolute;left:245px;top:44px;
    font-size:14.2px;color:var(--text-light);letter-spacing:.2px;text-transform:uppercase;
  }
  .cta-member{
    position:absolute;left:660px;top:32px;width:147px;height:34px;border-radius:7px;
    background:linear-gradient(180deg,var(--accent-yellow-light),var(--accent-yellow));
    font-family:'Montserrat',sans-serif;font-weight:700;font-size:11px;color:#2a2410;letter-spacing:.3px;
    display:flex;align-items:center;justify-content:center;text-decoration:none;
  }
  .main-nav{
    position:absolute;left:267px;top:82px;display:flex;gap:28px;font-size:14px;
  }
  .main-nav a{color:var(--text-light);text-decoration:none}
  .main-nav a.is-active{color:var(--nav-active)}
  .hero{
    position:absolute;left:33px;top:115px;width:770px;height:357px;overflow:hidden;
  }
  .hero-photo{
    position:absolute;inset:0;
    background:
      linear-gradient(180deg,#eef2e0 0%,#bcd08a 14%,#6f8f3a 30%,#a6a058 48%,#c9b56a 62%,#9a8a3e 80%,#c4c070 100%);
  }
  .hero-title{
    position:absolute;left:0;right:0;top:100px;text-align:center;
    font-family:'Alfa Slab One',serif;font-size:32px;font-weight:400;line-height:49px;color:var(--white);
    text-shadow:0 2px 4px rgba(0,0,0,.55);
  }
  .hero-dots{position:absolute;left:0;right:0;top:317px;display:flex;justify-content:center;gap:13px}
  .hero-dots span{width:11px;height:11px;border-radius:50%;border:1.5px solid var(--white)}
  .hero-dots span.is-current{background:var(--white)}
  .about{position:absolute;left:0;top:500px;width:836px;text-align:center}
  .section-title{font-family:'Alfa Slab One',serif;font-size:17px;color:var(--white);font-weight:400}
  .about p{font-size:11px;line-height:17px;color:var(--text-muted);margin-top:16px}
  .about p + p{margin-top:14px}
  .btn-grey{
    display:inline-flex;align-items:center;justify-content:center;
    border-radius:8px;background:linear-gradient(180deg,var(--button-grey-top),var(--button-grey-bottom));
    color:#222;font-size:11.5px;text-decoration:none;
  }
  .about .btn-grey{position:absolute;left:381px;top:143px;width:74px;height:29px}
  .rule-h{position:absolute;left:33px;width:770px;height:1px;background:var(--rule)}
  .rule-v{position:absolute;top:728px;width:1px;height:300px;background:var(--rule)}
  .col-title{position:absolute;top:746px}
  .event{position:absolute;left:34px;display:flex;gap:9px}
  .event-thumb{width:60px;height:53px;border:2px solid #555}
  .event-text{font-size:11.5px;line-height:17.5px;color:var(--text-muted);margin-top:-2px}
  .newsletter{position:absolute;left:314px;top:746px;width:200px}
  .newsletter p{font-size:11.5px;line-height:17px;color:var(--text-muted)}
  .newsletter .intro{margin-top:17px}
  .newsletter .contact-email{margin-top:17px}
  .field{
    display:flex;align-items:center;width:160px;height:31px;padding-left:9px;
    border:1px solid #5b5b58;background:#2d2d2b;color:var(--text-muted);font-size:11.5px;
  }
  .field-name{margin-top:20px}
  .field-email{margin-top:11px}
  .newsletter .btn-grey{margin-top:20px;width:60px;height:31px}
  .ad-slot{
    position:absolute;left:568px;top:752px;width:233px;height:247px;
    border:4px solid #4a4a48;
  }
  .ad-image{
    width:100%;height:100%;
    background:linear-gradient(135deg,#3b82a8 0%,#1f4f7a 40%,#e9eef5 62%,#2c5aa8 100%);
  }
  .footer-nav{position:absolute;left:33px;top:1064px;font-size:14px;color:var(--text-light)}
  .footer-nav a{color:var(--text-light);text-decoration:none}
  .footer-nav .sep{margin:0 4px;color:#aaa}
  .copyright{position:absolute;left:33px;top:1091px;font-size:11px;color:#cfcfcb}
  .cta-advertise{
    position:absolute;left:539px;top:1067px;width:129px;height:32px;border-radius:7px;
    background:linear-gradient(180deg,var(--accent-yellow-light),var(--accent-yellow));
    font-weight:700;font-size:12.5px;color:#2a2410;text-decoration:none;
    display:flex;align-items:center;justify-content:center;
  }
  .social{position:absolute;left:682px;top:1064px;display:flex;gap:7px}
  .social a{width:36px;height:36px;border-radius:50%;border:2px solid #bdbdb9;display:block}
</style>
</head>
<body>
  <div class="site">
    <header class="site-header">
      <div class="logo"><span class="logo-dot"></span>TMRCL</div>
      <div class="org-name">Texas Marsh Reed Conservation League</div>
      <a class="cta-member" href="#">BECOME A MEMBER</a>
      <nav class="main-nav">
        <a class="is-active" href="#">Home</a>
        <a href="#">About</a>
        <a href="#">Members</a>
        <a href="#">Resources</a>
        <a href="#">Events</a>
        <a href="#">Membership</a>
        <a href="#">Contact</a>
      </nav>
      <section class="hero">
        <div class="hero-photo" role="img" aria-label="Calm pond with floating lily pads and green trees under a bright sky"></div>
        <h1 class="hero-title">Promoting environmental Stewardship<br>through operations, Research, education<br>and outreach</h1>
        <div class="hero-dots"><span></span><span class="is-current"></span><span></span></div>
      </section>
    </header>

    <section class="about">
      <h2 class="section-title">About TMRCL</h2>
      <p>Texas Professional Women's Circle is an organization of professional female executives from many different professions and industries.</p>
      <p>We come together to network, share experiences and professional resources, and we are actively involved in the community.<br>encourage job creation and create opportunities in local and regional food systems.</p>
      <a class="btn-grey" href="#">Read More</a>
    </section>

    <div class="rule-h" style="top:716px"></div>
    <div class="rule-v" style="left:279px"></div>
    <div class="rule-v" style="left:523px"></div>

    <h2 class="section-title col-title" style="left:34px">Upcoming Events</h2>
    <div class="event" style="top:788px">
      <div class="event-thumb" role="img" aria-label="Blue sky over a green field at sunrise" style="background:linear-gradient(180deg,#2f6bb3,#8fb8e0 45%,#f1d56a 60%,#4d7a22)"></div>
      <div class="event-text">2014 TMRCL Conference<br>October 12-14<br>Bluestem Ranch</div>
    </div>
    <div class="event" style="top:861px">
      <div class="event-thumb" role="img" aria-label="Golden wheat field glowing in sunset light" style="background:linear-gradient(180deg,#f7e08a,#e0a02a 45%,#9a6414)"></div>
      <div class="event-text">2014 TMRCL Conference<br>October 12-14<br>Bluestem Ranch</div>
    </div>
    <div class="event" style="top:941px">
      <div class="event-thumb" role="img" aria-label="Hay bales on farmland under a hazy sky" style="background:linear-gradient(180deg,#d9d2a0,#a8a062 45%,#5d6a2c)"></div>
      <div class="event-text">2014 TMRCL Conference<br>October 12-14<br>Bluestem Ranch</div>
    </div>

    <div class="newsletter">
      <h2 class="section-title">Newsletter Signup</h2>
      <p class="intro">Promote Your Products &amp; Services<br>in Our Newsletter</p>
      <p class="contact-email">reedkeeper@marshmail.net</p>
      <div class="field field-name">Name</div>
      <div class="field field-email">Email Address</div>
      <a class="btn-grey" href="#">Sign Up</a>
    </div>

    <aside class="ad-slot">
      <div class="ad-image" role="img" aria-label="Member advertisement showing algaecide product packaging on a water background"></div>
    </aside>

    <div class="rule-h" style="top:1046px;height:2px"></div>
    <nav class="footer-nav">
      <a href="#">Home</a><span class="sep">/</span><a href="#">About</a><span class="sep">/</span><a href="#">Members</a><span class="sep">/</span><a href="#">Resources</a><span class="sep">/</span><a href="#">Events</a><span class="sep">/</span><a href="#">Membership</a><span class="sep">/</span><a href="#">Contact</a>
    </nav>
    <div class="copyright">Copyright © 2014 tmrcl.org. All rights reserved.</div>
    <a class="cta-advertise" href="#">Advertise with us</a>
    <div class="social">
      <a href="#" aria-label="Social profile one"></a>
      <a href="#" aria-label="Social profile two"></a>
      <a href="#" aria-label="Video channel"></a>
    </div>
  </div>
</body>
</html>
```